New Business Card Design Project for Handyman Business

I would like to purchase a customized version of a design you have previously submitted - https://www.artvelloshowcase.com/design/58172046
I love this design!
I am hoping you can design something similar to this for our Handyman Business.
Attached is our logo and some graphics we have used.
Here is a link to the Google Doc with the content that needs to be included, https://files.quorvandel.net/document/d/e/4QZTR-8kPw2LmXn5Hb7rYcVt-qaaJsK3Df9TgNpU4WeR__LmcXaBvKpHsd2Qjn7wo4tzhgrVb41K85o3ttSTq/pub
Target Market(s)
Real Estate Agents, Home Owners and Property Managers
Industry/Entity Type
Construction/ Speciality Trade
Contact Information for Business Card
https://files.quorvandel.net/document/d/7QwRtYpL_zxkn4BvHnCdFs8TmKjWaEr2LUXPo6cxhg/edit?usp=sharing
Font styles to use
Other font styles liked:
- Ubuntu
Look and feel
Each slider illustrates characteristics of the customer's brand and the style your logo design should communicate.

```html
<!DOCTYPE html>
<html lang="en">
<head>
<meta charset="utf-8">
<title>Brightnook Business Card</title>
<link href="https://fonts.googleapis.com/css2?family=Poppins:wght@400;500;600&display=swap" rel="stylesheet">
<style>
  :root {
    --backdrop: #2b2b2d;
    --card: #232326;
    --card-top: #1f1f22;
    --card-shade: #1b1b1d;
    --green: #3fb845;
    --blue: #2f7fc7;
    --ink: #f2f2f2;
    --rule: #4a4a4e;
    --photo-a: #3f7d3a;
    --photo-b: #4a8fcf;
  }
  * { box-sizing: border-box; margin: 0; padding: 0; }
  html, body { width: 1200px; height: 1108px; overflow: hidden; }
  body {
    background: var(--backdrop);
    font-family: "Poppins", sans-serif;
    color: var(--ink);
    position: relative;
  }
  .card {
    position: absolute;
    top: 200px;
    width: 420px;
    height: 708px;
    border-radius: 20px;
    background: var(--card);
    overflow: hidden;
    box-shadow: 0 18px 40px rgba(0,0,0,.45);
  }
  .card--front { left: 150px; }
  .card--back { left: 630px; }

  .facets { position: absolute; inset: 0; }

  .brand {
    position: absolute;
    left: 0; right: 0;
    text-align: center;
    font-family: "Poppins", sans-serif;
    font-weight: 600;
    font-size: 44px;
    line-height: 1;
    color: var(--green);
  }
  .card--front .brand { top: 130px; }
  .card--back .brand { top: 420px; }

  .portrait {
    position: absolute;
    left: 155px; top: 250px;
    width: 110px; height: 110px;
    background: linear-gradient(160deg, var(--photo-a) 0%, var(--photo-a) 50%, var(--photo-b) 100%);
  }
  .person {
    position: absolute;
    top: 380px; left: 0; right: 0;
    text-align: center;
  }
  .person__name {
    font-weight: 500;
    font-size: 22px;
    letter-spacing: 2px;
    color: var(--green);
  }
  .person__role {
    font-size: 15px;
    color: var(--blue);
    margin-top: 2px;
  }
  .divider {
    position: absolute;
    left: 50px; right: 50px; top: 450px;
    height: 1px;
    background: var(--rule);
  }
  .contact {
    position: absolute;
    top: 466px; left: 0; right: 0;
    text-align: center;
    font-size: 18px;
    line-height: 1.6;
    font-style: normal;
  }
  .band {
    position: absolute;
    left: 0; right: 0; top: 598px;
    height: 34px;
    background: var(--green);
    color: #111;
    font-size: 15px;
    font-style: italic;
    text-align: center;
    line-height: 34px;
  }
  .services {
    position: absolute;
    top: 648px; left: 0; right: 0;
    display: flex;
    justify-content: center;
    gap: 14px;
    font-size: 14px;
    font-weight: 500;
  }
  .services li { list-style: none; display: flex; align-items: center; gap: 6px; }
  .services li::before {
    content: "";
    width: 9px; height: 9px;
    background: var(--green);
    transform: rotate(45deg);
  }

  .socials {
    position: absolute;
    top: 500px; left: 40px; right: 40px;
    display: flex;
    align-items: center;
    justify-content: center;
    gap: 18px;
  }
  .socials__line { flex: 1; height: 1px; background: var(--green); }
  .socials__badge {
    width: 22px; height: 22px;
    border: 1.5px solid var(--green);
    transform: rotate(45deg);
  }
  .hashtag {
    position: absolute;
    top: 545px; left: 0; right: 0;
    text-align: center;
    font-size: 16px;
    letter-spacing: .5px;
  }
</style>
</head>
<body>

<section class="card card--front" aria-label="Business card front">
  <svg class="facets" viewBox="0 0 420 708" aria-hidden="true">
    <polygon points="0,0 420,0 420,210 300,300 120,300 0,210" fill="var(--card-top)"/>
    <polygon points="0,330 100,300 70,420 0,470" fill="var(--card-shade)"/>
    <polygon points="420,330 320,300 350,420 420,470" fill="var(--card-shade)"/>
  </svg>

  <p class="brand">brightnook</p>

  <div class="portrait" role="img" aria-label="Portrait photo of the owner outdoors among greenery"></div>

  <div class="person">
    <h1 class="person__name">HOLLIS CRANE</h1>
    <p class="person__role">Owner/ Handyman</p>
  </div>

  <div class="divider"></div>

  <address class="contact">
    (555) 214-3307<br>
    hollis@brightnook.com<br>
    Brightnook.com
  </address>

  <div class="band">Commercial and Residential Handyman</div>

  <ul class="services">
    <li>Improve</li>
    <li>Repair</li>
    <li>Remodel</li>
    <li>Maintain</li>
  </ul>
</section>

<section class="card card--back" aria-label="Business card back">
  <p class="brand">brightnook</p>

  <div class="socials" aria-label="Social media links">
    <span class="socials__line"></span>
    <span class="socials__badge"></span>
    <span class="socials__badge"></span>
    <span class="socials__badge"></span>
    <span class="socials__badge"></span>
    <span class="socials__line"></span>
  </div>

  <p class="hashtag">#BrightnookHandymanServices</p>
</section>

</body>
</html>
```